Personal Trainer website design

We are working with a personal trainer to design a website. They offer their primary services: Diet Coaching, In-Person Coaching (workouts), and Remote Coaching.
Some sites we like: https://www.marenkoltby.com, https://tavilobrenn.com/en-us, https://corevandel.co.uk
Thank you for taking the time to consider designing a website for us. We are web developers based in Stockton, CA USA. Most of our projects go through the same process. Understanding this process may help you win a project with us. We custom-code all of our websites in-house. We don’t have any requirements as to what tools you use for your design, but ask that you follow these guidelines.
IMAGES:
We ask that if you use any images, or icons in the design, have a link to the asset, so we can purchase the image/icon. Most of the designs we submit do not have the customer’s images on them unless they have some great images. Be creative; show us the feeling that you are trying to portray with your image choices. Use any royalty-free site you choose. We subscribe to Quillex and mostly use their images, but are ok to purchase images outside of Quillex.
FONTS:
We ask that you identify the fonts you’re using in the design. This can be done in a message if you want. We typically use Brimora Fonts and Quillex Fonts.
CONTENT:
We're always open to different content and ideas. Often, we submit designs with stock images so that the client can see our vision. We typically go back and take pictures after the website launch to use their images with our vision. Lorem Ipsum is fine for paragraphs, but we ask that you make the Headers with correct English. We want to be able to show the vision and identify the sections of the website.
INSPIRATION:
We try and add a couple of links in the brief of some websites that we like to help you get started in your design.
REVISIONS:
We do not often ask for revisions of the designs unless we see something in the design that may not appeal to the client. If there are slight changes that we want to make, we simply do that in the development process.
FEEDBACK:
We rarely give feedback on designs during the design process. We are working on many website projects and do not have the time to give feedback. We usually respond if your request is well thought out and asks specific questions, but a note asking “feedback, please” usually goes unanswered.
1 page

```html
<!DOCTYPE html>
<html lang="en">
<head>
<meta charset="utf-8">
<title>Veltra Fit — Personal Training</title>
<link href="https://fonts.googleapis.com/css2?family=Teko:wght@400;500;600&family=Poppins:wght@400;500;600&display=swap" rel="stylesheet">
<style>
:root{
  --sidebar:#000;
  --base:#2b2a28;
  --deep:#181818;
  --footer:#222120;
  --olive:#8b9a1e;
  --khaki:#6f6548;
  --text:#ffffff;
  --muted:#cfcbbf;
  --line:#8f8665;
}
*{margin:0;padding:0;box-sizing:border-box}
html,body{width:1200px;height:5146px;overflow:hidden}
body{position:relative;background:var(--base);color:var(--text);font-family:"Poppins",sans-serif}
.abs{position:absolute}
.head{font-family:"Teko",sans-serif;font-weight:500;letter-spacing:.5px;line-height:1}
.olive{color:var(--olive)}
.photo{position:absolute}
.btn{position:absolute;display:flex;align-items:center;justify-content:center;font-size:11px;font-weight:600;letter-spacing:.6px;text-transform:uppercase;color:#fff}
.btn-olive{background:var(--olive)}
.btn-khaki{background:var(--khaki)}
.btn-frame::after{content:"";position:absolute;left:5px;top:5px;right:-5px;bottom:-5px;border-right:2px solid #d8d4c4;border-bottom:2px solid #d8d4c4}

/* sidebar */
.sidebar{left:0;top:0;width:162px;height:5146px;background:var(--sidebar)}
.brand{display:flex;align-items:center;gap:8px;font-family:"Teko",sans-serif;font-weight:500;color:#fff}
.nav a{position:absolute;left:0;width:162px;text-align:center;font-size:10.5px;font-weight:500;letter-spacing:.5px;color:#fff;text-decoration:none;text-transform:uppercase}
.nav a.current{color:var(--olive);text-decoration:underline}

/* sections */
.band{position:absolute;left:162px;width:1038px}
.dots{left:544px;top:36px;width:118px;height:166px;background-image:radial-gradient(circle,#bdb9ad 2px,transparent 2.5px);background-size:16.6px 16.6px}

.feature{position:absolute;left:672px;display:flex;gap:20px;align-items:center;font-size:11px;line-height:1.55;color:#e8e6df;width:400px}
.diamond{width:30px;height:30px;background:var(--olive);transform:rotate(45deg);flex:none;margin-left:6px;display:flex;align-items:center;justify-content:center}
.diamond span{width:12px;height:12px;border:2px solid #fff;transform:rotate(-45deg)}

.plan{position:absolute;top:1798px;width:278px;height:348px;background:var(--khaki);text-align:center}
.plan .tier{margin-top:34px;font-size:13px;letter-spacing:1px;color:#e6e2d6}
.plan .offer{margin-top:18px;font-family:"Teko",sans-serif;font-size:24px;color:#fff}
.plan .note{margin-top:10px;font-size:10px;line-height:1.8;color:#d8d3c2;height:38px}
.plan hr{border:0;border-top:1px solid #8a8163;margin:20px 26px 0}
.plan .price{margin-top:20px;font-family:"Teko",sans-serif;font-size:44px;font-weight:600}
.plan .per{font-size:10px;color:#d8d3c2;margin-top:-8px}
.plan .btn{position:relative;margin:10px auto 0;width:166px;height:32px;font-size:9.5px}

.class-card{position:absolute;top:2334px;width:338px;height:410px;text-align:center}
.class-card .title{position:absolute;left:0;right:0;font-size:19px;font-weight:600;line-height:1.2}
.class-card .desc{position:absolute;left:60px;right:60px;font-size:10.5px;line-height:1.6;color:#eee}
.class-card .btn{left:100px;width:138px;height:32px;font-size:9.5px;border:2px solid #fff}

.badge{position:absolute;top:4670px;width:96px;height:96px;border:3px solid #fff;border-radius:50%}

.store{position:absolute;top:4344px;height:42px;border:1.5px solid #fff;border-radius:6px;background:#000;display:flex;align-items:center;gap:8px;padding:0 12px}
.store i{width:18px;height:18px;border-radius:50%;background:#fff;display:block}
.store small{display:block;font-size:8px;color:#ddd}
.store b{display:block;font-size:14px;font-weight:500}

.footer-links a{color:#fff;text-decoration:none;font-size:11px;margin-right:14px}
.social{position:absolute;top:5002px;width:24px;height:24px;border-radius:50%;background:var(--khaki)}
</style>
</head>
<body>

<!-- sidebar -->
<aside class="abs sidebar">
  <div class="abs brand" style="left:24px;top:62px;font-size:30px"><span style="width:14px;height:14px;border-radius:50%;background:var(--olive)"></span>VELTRA FIT</div>
  <nav class="nav">
    <a class="current" style="top:156px">Home</a>
    <a style="top:196px">Services</a>
    <a style="top:234px">About</a>
    <a style="top:274px">Shop</a>
    <a style="top:312px">Reviews</a>
    <a style="top:352px">Contact us</a>
  </nav>
  <div class="btn" style="left:32px;top:424px;width:94px;height:26px;border:2px solid #fff;font-size:10px">Login</div>
  <div class="btn btn-olive" style="left:32px;top:470px;width:94px;height:24px;font-size:10px">Register</div>
</aside>

<!-- hero -->
<div class="abs dots"></div>
<h1 class="abs head" style="left:268px;top:290px;font-size:50px;line-height:48px">
  <span class="olive">MOVE YOUR</span><br><span class="olive">BODY,</span> SHAPE<br>YOUR FUTURE
</h1>
<div class="btn btn-olive btn-frame" style="left:268px;top:464px;width:162px;height:44px">Find gyms
  <svg width="22" height="10" viewBox="0 0 22 10" style="margin-left:10px"><path d="M0 5h20M15 1l5 4-5 4" stroke="#fff" stroke-width="1.6" fill="none"/></svg>
</div>
<div class="photo" role="img" aria-label="Athletic woman in black workout top posing in a dark gym" style="left:612px;top:86px;width:400px;height:598px;background:linear-gradient(160deg,#4b4843,#1d1c1b 70%)"></div>
<div class="btn btn-olive" style="left:848px;top:464px;width:352px;height:54px;justify-content:flex-start;padding-left:30px;font-size:12px">
  <svg width="12" height="15" viewBox="0 0 12 15" style="margin-right:10px"><path d="M6 0a6 6 0 0 0-6 6c0 4 6 9 6 9s6-5 6-9a6 6 0 0 0-6-6z" fill="#fff"/><circle cx="6" cy="6" r="2.2" fill="var(--olive)"/></svg>Enter your location now
</div>
<div class="abs" style="left:746px;top:518px;width:454px;height:94px;background:var(--khaki);padding:20px 38px;font-size:17px;line-height:28px;letter-spacing:.4px">New Membership Deals Going On!<br>Join Now For $0 Initiation.</div>

<!-- community -->
<div class="photo" role="img" aria-label="Smiling man in a black tank top sitting and making an OK gesture" style="left:240px;top:790px;width:360px;height:430px;background:radial-gradient(ellipse at 50% 55%,#5c544a,#2b2a28 70%)"></div>
<h2 class="abs head" style="left:672px;top:790px;font-size:40px">OUR <span class="olive">COMMUNITY</span></h2>
<p class="abs" style="left:672px;top:840px;width:420px;font-size:11.5px;line-height:1.6;font-weight:500">Lorem ipsum dolor sit amet, consetetur sadipscing elitr sed diam nonumy eirmod tempor invidunt ut labore et</p>
<div class="feature" style="top:906px"><div class="diamond"><span></span></div>Sed diam nonumy eirmod tempor invidunt ut labore et dolore magna aliquyam erat.</div>
<div class="feature" style="top:968px"><div class="diamond"><span></span></div>Sed diam nonumy eirmod tempor invidunt ut labore et dolore magna aliquyam erat.</div>
<div class="feature" style="top:1030px"><div class="diamond"><span></span></div>Sed diam nonumy eirmod tempor invidunt ut labore et dolore magna aliquyam erat.</div>
<div class="feature" style="top:1092px"><div class="diamond"><span></span></div>Sed diam nonumy eirmod tempor invidunt ut labore et dolore magna aliquyam erat.</div>
<div class="btn btn-khaki btn-frame" style="left:672px;top:1170px;width:206px;height:40px">Gyms where you are</div>
<div class="btn btn-olive btn-frame" style="left:904px;top:1170px;width:156px;height:40px">Subscribe now</div>

<!-- book class -->
<section class="band" role="img" aria-label="Dim gym floor with kettlebells and an athlete doing push-ups" style="top:1328px;height:284px;background:linear-gradient(90deg,#1d1d1c,#3a3835 50%,#1d1d1c)"></section>
<div class="abs head" style="left:162px;width:1038px;top:1394px;text-align:center;font-size:34px;line-height:36px">BOOK CLASS<br>FLEXIBLE PASS <span class="olive">CANCEL ANY TIME</span></div>
<svg class="abs" style="left:508px;top:1488px" width="44" height="44" viewBox="0 0 44 44"><path d="M9 6l7 7-4 5c3 6 8 11 14 14l5-4 7 7-5 6C20 40 4 24 4 11z" fill="none" stroke="var(--olive)" stroke-width="2"/><path d="M26 8a11 11 0 0 1 10 10M26 2a17 17 0 0 1 16 16" fill="none" stroke="var(--olive)" stroke-width="2"/></svg>
<div class="abs" style="left:582px;top:1484px;font-size:13px;font-weight:600">MAKE A CALL</div>
<div class="abs head olive" style="left:582px;top:1504px;font-size:36px">(+00) 555 014 278</div>

<!-- pricing -->
<h2 class="abs head" style="left:162px;width:1038px;top:1712px;text-align:center;font-size:42px">PRICING <span class="olive">PLAN</span></h2>
<div class="plan" style="left:236px"><div class="tier">BRONZE</div><div class="offer">First class free</div><div class="note">First time users only<br>Live classes</div><hr><div class="price">$0,00</div><div class="per">&nbsp;</div><div class="btn btn-olive btn-frame">Get your free class</div></div>
<div class="plan" style="left:536px"><div class="tier">SILVER</div><div class="offer">7 Day free trial</div><div class="note">Lorem ipsum dolor sit amet<br>consectet adipiscing</div><hr><div class="price">$100</div><div class="per">/Per month</div><div class="btn btn-olive btn-frame">Start your trial</div></div>
<div class="plan" style="left:836px"><div class="tier">PLATINUM</div><div class="offer">7 Day free trial</div><div class="note">Lorem ipsum dolor sit amet<br>consectet adipiscing</div><hr><div class="price">$150</div><div class="per">/Per month</div><div class="btn btn-olive btn-frame">Start your trial</div></div>

<!-- classes -->
<h2 class="abs head" style="left:162px;width:1038px;top:2248px;text-align:center;font-size:42px">CLASSES</h2>
<div class="class-card" style="left:162px">
  <div class="photo" role="img" aria-label="Woman holding an apple for diet coaching" style="inset:0;background:linear-gradient(180deg,#8a8580,#4a4744 55%,#2c2b29)"></div>
  <div class="title" style="top:128px">DIET COACHING</div>
  <div class="desc" style="top:162px">Sed do eiusmod tempor incididu labo dolore magna aliqua enim.</div>
  <div class="btn" style="top:226px">View details</div>
</div>
<div class="class-card" style="left:512px">
  <div class="photo" role="img" aria-label="Man lifting a loaded barbell in a gym" style="inset:0;background:linear-gradient(180deg,#6d6a66,#3d3b38 55%,#242322)"></div>
  <div class="title" style="top:118px">PERSON COACHING<br>(WORKOUTS)</div>
  <div class="desc" style="top:174px">Sed do eiusmod tempor incididu labo dolore magna aliqua enim.</div>
  <div class="btn btn-olive" style="top:238px;border:none">View details</div>
</div>
<div class="class-card" style="left:862px">
  <div class="photo" role="img" aria-label="Smiling man sitting on a mat with a laptop for remote coaching" style="inset:0;background:linear-gradient(180deg,#7c766c,#48443d 55%,#2a2825)"></div>
  <div class="title" style="top:128px">REMOTE COACHING</div>
  <div class="desc" style="top:162px">Sed do eiusmod tempor incididu labo dolore magna aliqua enim.</div>
  <div class="btn" style="top:226px">View details</div>
</div>

<!-- about -->
<div class="abs" style="left:256px;top:2902px;width:360px;height:362px;background:var(--khaki)"></div>
<div class="abs" style="left:278px;top:2926px;width:314px;height:314px;border:1.5px solid var(--olive)"></div>
<div class="photo" role="img" aria-label="Woman and man trainers standing back to back with arms crossed" style="left:268px;top:2850px;width:336px;height:390px;background:radial-gradient(ellipse at 50% 55%,#8f887a,#6f6548 72%,rgba(111,101,72,0) 73%)"></div>
<div class="abs" style="left:664px;top:2940px;font-size:12px;font-weight:500;letter-spacing:.6px">ABOUT US</div>
<div class="abs head" style="left:664px;top:2962px;font-size:40px">VELTRA FIT</div>
<p class="abs" style="left:664px;top:3024px;width:452px;font-size:11px;line-height:20px;color:#e4e1d8">Lorem ipsum dolor sit amet, consectetur adipisicing elit, sed do eiusmod tempor incididunt ut labore et dolore magna aliqua. Ut enim ad minim veniam, quis nostrud exercitation ullamco laboris nisi ut aliquip ex ea commodo consequat. Duis aute irure dolor in reprehenderit in voluptate velit esse cillum dolore eu fugiat nulla pariatur. Excepteur sint occaecat cupidatat non proident.</p>
<div class="btn btn-olive btn-frame" style="left:664px;top:3180px;width:186px;height:42px">Learn more
  <svg width="22" height="10" viewBox="0 0 22 10" style="margin-left:10px"><path d="M0 5h20M15 1l5 4-5 4" stroke="#fff" stroke-width="1.6" fill="none"/></svg>
</div>

<!-- testimonials -->
<section class="band" style="top:3368px;height:578px;background:var(--deep)"></section>
<h2 class="abs head" style="left:162px;width:1038px;top:3468px;text-align:center;font-size:42px">WHAT OUR <span class="olive">CLIENTS SAY</span></h2>
<div class="abs" style="left:318px;top:3556px;width:728px;height:146px;background:var(--khaki);padding:36px 60px;text-align:center;font-style:italic;font-size:14px;line-height:24px">
  <span style="font-family:'Teko',sans-serif;font-size:30px;font-style:normal;vertical-align:-8px">&ldquo;</span> Lorem ipsum dolor sit amet, consectetur adipisicing elit sed do eiusmod tempor incididunt ut labore et dolore magna aliqua Ut enim ad minim veniam quis nostrud exercitation ullamco laboris nisi ut aliquip <span style="font-family:'Teko',sans-serif;font-size:30px;font-style:normal;vertical-align:-14px">&rdquo;</span>
</div>
<svg class="abs" style="left:664px;top:3700px" width="36" height="18" viewBox="0 0 36 18"><path d="M0 0h36L18 18z" fill="var(--khaki)"/></svg>
<div class="abs" style="left:162px;width:1038px;top:3752px;text-align:center;font-size:17px;font-weight:500;letter-spacing:1px">DARA QUELL</div>
<svg class="abs" style="left:638px;top:3826px" width="90" height="20" viewBox="0 0 90 20"><circle cx="6" cy="10" r="4" fill="#bbb"/><circle cx="22" cy="10" r="7" fill="var(--olive)"/><circle cx="38" cy="10" r="4" fill="#bbb"/><circle cx="52" cy="10" r="4" fill="#bbb"/><circle cx="66" cy="10" r="4" fill="#bbb"/><circle cx="80" cy="10" r="4" fill="#bbb"/></svg>

<!-- app -->
<svg class="abs" style="left:258px;top:4124px" width="360" height="350" viewBox="0 0 360 350">
  <circle cx="198" cy="175" r="170" fill="none" stroke="var(--olive)" stroke-width="3"/>
  <circle cx="198" cy="175" r="150" fill="var(--olive)"/>
</svg>
<div class="abs" style="left:340px;top:4048px;width:232px;height:470px;border-radius:30px;background:#111;border:3px solid #3a3a3a"></div>
<div class="abs" style="left:352px;top:4060px;width:208px;height:446px;border-radius:22px;background:#fff;color:#111;text-align:center">
  <div style="margin-top:58px;font-size:12px;font-weight:500;line-height:1.4">Select your plan to<br>get started</div>
  <div role="img" aria-label="Woman training with a dumbbell on a bench" style="margin:20px auto 0;width:170px;height:170px;border-radius:6px;background:linear-gradient(160deg,#b8aa96,#5c4e42)"></div>
  <div style="margin-top:10px;font-size:16px;color:var(--olive);letter-spacing:4px">● ● ●</div>
  <div style="margin:28px 24px 0;font-size:6.5px;line-height:1.5;color:#333">Lorem ipsum dolor sit amet, consetetur sadipscing elitr, sed diam</div>
  <div style="margin:30px auto 0;width:170px;height:28px;border-radius:8px;background:var(--olive);color:#fff;font-size:9px;font-weight:600;display:flex;align-items:center;justify-content:center">NEXT</div>
</div>
<h2 class="abs head" style="left:696px;top:4170px;font-size:42px">DOWNLOAD <span class="olive">THE APP</span></h2>
<p class="abs" style="left:696px;top:4232px;width:420px;font-size:11px;line-height:20px;color:#e4e1d8">Lorem ipsum dolor sit amet, consetetur sadipscing elitr, sed diam nonumy eirmod tempor invidunt ut labore et dolore magna aliquyam erat, sed diam voluptua. At vero eos et accusam et justo.</p>
<div class="store" style="left:696px"><i></i><span><small>Download on the</small><b>Appvault</b></span></div>
<div class="store" style="left:836px"><i></i><span><small>GET IT ON</small><b>Playdeck</b></span></div>

<!-- partners -->
<section class="band" style="top:4620px;height:198px;background:var(--olive)"></section>
<div class="badge" style="left:250px"></div>
<div class="badge" style="left:456px"></div>
<div class="badge" style="left:642px"></div>
<div class="badge" style="left:822px"></div>
<div class="badge" style="left:1026px"></div>

<!-- footer -->
<section class="band" style="top:4818px;height:328px;background:var(--footer)"></section>
<div class="abs brand" style="left:236px;top:4950px;font-size:64px"><span style="width:30px;height:30px;border-radius:50%;background:var(--olive)"></span>VELTRA FIT</div>
<div class="abs footer-links" style="left:536px;top:4944px"><a>Home</a><a>Services</a><a>About</a><a>Shop</a><a>Reviews</a><a>Contact us</a></div>
<div class="abs footer-links" style="left:536px;top:4972px"><a style="margin-right:30px">Privacy Policy</a><a>Terms and Conditions</a></div>
<div class="social" style="left:536px"></div>
<div class="social" style="left:566px"></div>
<div class="social" style="left:596px"></div>
<div class="social" style="left:626px"></div>
<div class="abs" style="left:536px;top:5062px;font-size:11px">Copyright 2023 VELTRAFIT. All Rights Reserved.</div>
<div class="abs head" style="left:944px;top:4940px;font-size:22px">Subscribe our newsletter</div>
<div class="abs" style="left:944px;top:4980px;width:218px;height:26px;border:1px solid #bbb;font-size:10px;padding:6px 14px;color:#ddd">Email address</div>
<div class="btn btn-olive" style="left:944px;top:5016px;width:122px;height:30px;font-size:9.5px">Subscribe</div>

</body>
</html>
```